We are looking for a simple design that would be uplifting for
upscale drug addicts

MERIDIAN CIRCLE

PLEASE SEE THE LINK FOR TAG LINE AND CONTENT

thank you.

here is all the actual info we need and we want something like this...

http://assets.qlm.brivostore.com/rest/items/7c2910e5b337de81f94a02bd57e644163ab9fe0a6712?uid=bd31c9e2f7a04c18b6e0d44721fa93c5%2fdrafts&expires=1408211537&signature=kTp4WmQxNvLzHa8YbEoRcJsGf2B%3d

The shape and colors don't have to be like what I posted it is only an example.

Target Market(s)

Wall Street, internet and creative types, men, early 30's,
upwardly mobile, drug addicts

current site

bkltornavel.com

now launching new name Meridian Circle

Industry/Entity Type

Drug

Requirements
Must have
• upscale look, great font
Should not have
• a corporate look but should not look like a clinic.

```html
<!DOCTYPE html>
<html lang="en">
<head>
<meta charset="utf-8">
<title>Meridian Circle — Business Card</title>
<link rel="stylesheet" href="https://fonts.googleapis.com/css2?family=Questrial&family=Arimo:ital,wght@0,400;0,700;1,400&display=swap">
<style>
  :root {
    --brand-red: #d7222c;
    --ink: #111111;
    --paper: #ffffff;
    --swoosh-light: #ffffff;
    --swoosh-dark: #b9b9b9;
  }
  * { margin: 0; padding: 0; box-sizing: border-box; }
  html, body {
    width: 1200px; height: 315px; overflow: hidden;
    background: var(--paper);
  }
  .sheet { position: relative; width: 1200px; height: 315px; }

  .card { position: absolute; top: 0; height: 315px; }
  .card--front { left: 0; width: 612px; }
  .card--back { left: 643px; width: 557px; }

  .swoosh { position: absolute; left: 0; top: 0; }

  .brand-name {
    position: absolute;
    font-family: "Questrial", "Century Gothic", sans-serif;
    font-weight: 400;
    letter-spacing: 0.5px;
    white-space: nowrap;
  }
  .tagline {
    position: absolute;
    font-family: "Arimo", Arial, sans-serif;
    line-height: 1.15;
  }

  .card--front .brand-name { left: 26px; top: 26px; font-size: 37px; color: var(--ink); }
  .card--front .tagline { left: 26px; top: 80px; width: 360px; font-size: 17px; font-style: italic; color: var(--ink); }

  .contact {
    position: absolute; left: 26px; top: 152px;
    font-family: "Arimo", Arial, sans-serif;
    font-size: 14px; line-height: 1.1; color: var(--ink);
  }
  .contact__name { font-weight: 700; font-size: 16px; margin-bottom: 9px; }
  .email {
    position: absolute; left: 26px; top: 276px;
    font-family: "Arimo", Arial, sans-serif; font-size: 16px; color: var(--ink);
  }
  .phones {
    position: absolute; left: 454px; top: 260px;
    font-family: "Arimo", Arial, sans-serif; font-size: 16px; line-height: 1.4; color: var(--ink);
  }

  .band {
    position: absolute; left: 0; top: 193px; width: 557px; height: 90px;
    background: var(--brand-red);
  }
  .card--back .brand-name { left: 20px; top: 198px; font-size: 33px; color: var(--paper); }
  .card--back .tagline { left: 20px; top: 242px; width: 330px; font-size: 16px; color: var(--paper); }
</style>
</head>
<body>
<main class="sheet">
  <section class="card card--front">
    <svg class="swoosh" width="612" height="180" viewBox="0 0 612 180" aria-hidden="true">
      <defs>
        <linearGradient id="swooshFade" x1="0" y1="0" x2="1" y2="0.4">
          <stop offset="0" stop-color="var(--swoosh-light)"/>
          <stop offset="1" stop-color="var(--swoosh-dark)"/>
        </linearGradient>
      </defs>
      <path d="M250 0 H612 V130 C560 60 470 30 380 55 C330 68 290 40 250 0 Z" fill="url(#swooshFade)"/>
    </svg>
    <div class="brand-name">Meridian Circle</div>
    <p class="tagline">We don't cut any corners when it comes to your longterm recovery</p>
    <div class="contact">
      <p class="contact__name">Daniel Corvell, CASAC</p>
      <p>Program Coordinator</p>
      <p>418 W. 37th St. Suite 302</p>
      <p>New York, NY 10018</p>
    </div>
    <p class="email">counselor@harborlinewellness.com</p>
    <div class="phones">
      <p>212.555.0148</p>
      <p>212.555.0149</p>
    </div>
  </section>

  <section class="card card--back">
    <div class="band"></div>
    <div class="brand-name">Meridian Circle</div>
    <p class="tagline">We don't cut any corners when it comes to your longterm recovery</p>
  </section>
</main>
</body>
</html>
```